Event Graphics Needed for Young Adult Retreat

I need graphics designed for our summer young adult retreat for those 18 years old - 30 years old. This event will take place in the black hills of South Dakota. Primary graphic design is for a 11x17 poster but will also need the images resized for needs.
11x17 main poster design should include the following:
-Main Title: SD BrightPath logo & text (or logo only) presents . . . Summit Young Adult Gathering
-Dates: June 23-25th, 2023
-Register at SDBrightPath.example
-Pine Hollow Lodge Center, Deadwood, SD
-Speaker: Tom Velling (photo attached)
-Include SD BrightPath logo
-Event Graphic should be attractive to 18-30 year olds but SHOULD NOT include references to alcohol, sexuality, drugs, or profanity.
-please include a version with cut and bleed lines and a version without
-social media:
-square; can include only main titles, or main titles and speaker.
-include SD BrightPath logo
-16x9 title slide that includes:
-titles, full background images, organization logo. No camp speaker or dates, no additional info.
- a postcard size (3.5in X 5in)
-include all content on it
All graphics need to be print quality (300 dpi or higher)
My graphic design experience is limited. I will need help receiving the files I need in the various sizes. Thank you.

```html
<!DOCTYPE html>
<html lang="en">
<head>
<meta charset="utf-8">
<title>Summit Young Adult Gathering</title>
<link href="https://fonts.googleapis.com/css2?family=Archivo+Black&family=Arimo:wght@400;700&display=swap" rel="stylesheet">
<style>
:root{
  --sky:#2ec4f1;
  --sun:#fdd406;
  --amber:#f8a81c;
  --ink:#1f1a17;
  --navy:#1d2b3a;
  --paper:#ffffff;
  --backdrop:#e4e4e4;
  --soft-tri:#f0cf5c;
}
*{margin:0;padding:0;box-sizing:border-box}
html,body{width:964px;height:1200px;overflow:hidden;background:var(--backdrop)}
.poster{position:absolute;left:111px;top:20px;width:741px;height:1160px;background:var(--paper)}
.block{position:absolute}
.sky-corner{left:401px;top:0;width:340px;height:350px;background:var(--sky)}
.presents{position:absolute;left:46px;top:78px;font:30px/1 'Archivo Black',sans-serif;color:var(--ink);transform:rotate(-4deg);transform-origin:left bottom;white-space:nowrap}
.title{position:absolute;left:40px;top:118px;transform:rotate(-4deg);transform-origin:left top}
.title-band{display:block;width:max-content;font:62px/1 'Archivo Black',sans-serif;letter-spacing:-1px;color:var(--ink);padding:10px 14px 6px 12px;text-transform:uppercase}
.band-one{background:var(--sun)}
.band-two{background:var(--amber);margin-left:10px}
.band-three{background:var(--sun);margin-left:18px}
.tri{position:absolute}
.photo{left:106px;top:350px;width:636px;height:386px;background:linear-gradient(160deg,#cdd2c8 0%,#b59a7e 45%,#7e5c45 75%,#8ea2b4 100%)}
.amber-side{left:-9px;top:365px;width:115px;height:371px;background:var(--amber)}
.dots{position:absolute;left:-9px;top:590px}
.sun-corner{left:482px;top:736px;width:259px;height:302px;background:var(--sun)}
.speaker-frame{left:423px;top:838px;width:276px;height:166px;background:var(--sky)}
.speaker-photo{left:470px;top:785px;width:192px;height:219px;background:linear-gradient(180deg,#b98b6e 0%,#9a7560 40%,#5b6778 60%,#4d5a6c 100%);border-radius:90px 90px 0 0}
.ring{position:absolute;left:645px;top:760px}
.details{position:absolute;left:44px;top:800px;color:var(--ink)}
.row{display:flex;align-items:flex-start;gap:13px}
.date{font:32px/1.2 'Archivo Black',sans-serif}
.venue{font:22px/1.4 'Archivo Black',sans-serif;margin-top:10px}
.speaker{margin-top:18px}
.speaker-label{font:400 17px/1 'Arimo',sans-serif}
.speaker-name{font:700 20px/1 'Arimo',sans-serif;margin-top:13px;letter-spacing:.3px}
.footer-sun{left:-9px;top:1038px;width:199px;height:122px;background:var(--sun);display:flex;align-items:center;justify-content:center}
.brand{font:700 22px/1 'Arimo',sans-serif;color:var(--navy)}
.footer-sky{left:190px;top:1038px;width:551px;height:122px;background:var(--sky)}
.register{position:absolute;left:52px;top:26px;color:var(--navy)}
.register-lead{font:400 27px/1 'Arimo',sans-serif}
.register-url{font:700 34px/1.1 'Arimo',sans-serif;margin-top:2px}
</style>
</head>
<body>
<div class="poster">
  <div class="block sky-corner"></div>

  <div class="presents">SD BrightPath Presents</div>
  <h1 class="title">
    <span class="title-band band-one">Summit</span>
    <span class="title-band band-two">Young Adult</span>
    <span class="title-band band-three">Gathering</span>
  </h1>

  <svg class="tri" style="left:5px;top:278px" width="24" height="26" viewBox="0 0 24 26"><polygon points="0,0 24,13 0,26" fill="#fdd406"/></svg>
  <svg class="tri" style="left:630px;top:210px" width="62" height="64" viewBox="0 0 62 64"><polygon points="62,0 62,64 0,27" fill="#fdd406"/></svg>

  <div class="block amber-side"></div>
  <svg class="dots" width="60" height="92" viewBox="0 0 60 92">
    <g fill="#fdd406">
      <circle cx="4" cy="5" r="4.5"/><circle cx="30" cy="5" r="4.5"/><circle cx="56" cy="5" r="4.5"/>
      <circle cx="4" cy="31" r="4.5"/><circle cx="30" cy="31" r="4.5"/><circle cx="56" cy="31" r="4.5"/>
      <circle cx="4" cy="58" r="4.5"/><circle cx="30" cy="58" r="4.5"/><circle cx="56" cy="58" r="4.5"/>
      <circle cx="4" cy="84" r="4.5"/><circle cx="30" cy="84" r="4.5"/><circle cx="56" cy="84" r="4.5"/>
    </g>
  </svg>
  <div class="block photo" role="img" aria-label="Group photo of five smiling young adults outdoors"></div>

  <div class="block sun-corner"></div>
  <svg class="ring" width="56" height="56" viewBox="0 0 56 56"><circle cx="28" cy="28" r="26" fill="none" stroke="#fff" stroke-width="2"/></svg>
  <div class="block speaker-frame"></div>
  <div class="block speaker-photo" role="img" aria-label="Portrait photo of speaker Tom Velling"></div>

  <div class="details">
    <div class="row">
      <svg width="26" height="26" viewBox="0 0 26 26" style="margin-top:6px"><rect x="1" y="4" width="24" height="20" rx="2" fill="#f8a81c"/><rect x="6" y="1" width="3" height="6" fill="#f8a81c"/><rect x="17" y="1" width="3" height="6" fill="#f8a81c"/><g fill="#fff"><rect x="5" y="12" width="3" height="3"/><rect x="10" y="12" width="3" height="3"/><rect x="15" y="12" width="3" height="3"/><rect x="20" y="12" width="2" height="3"/><rect x="5" y="17" width="3" height="3"/><rect x="10" y="17" width="3" height="3"/><rect x="15" y="17" width="3" height="3"/></g></svg>
      <div class="date">June 23-25th, 2023</div>
    </div>
    <div class="row venue">
      <svg width="26" height="26" viewBox="0 0 26 26" style="margin-top:3px"><circle cx="13" cy="12" r="10" fill="none" stroke="#f8a81c" stroke-width="3"/><path d="M6 18 L13 25 L20 18 Z" fill="#f8a81c"/><circle cx="13" cy="12" r="3.5" fill="#f8a81c"/></svg>
      <div>Pine Hollow Lodge Center,<br>Deadwood, SD</div>
    </div>
    <div class="row speaker">
      <svg width="22" height="32" viewBox="0 0 22 32" style="margin-left:2px"><rect x="6" y="0" width="10" height="19" rx="5" fill="#f8a81c"/><path d="M2 13 a9 9 0 0 0 18 0" fill="none" stroke="#f8a81c" stroke-width="2.5"/><line x1="11" y1="22" x2="11" y2="29" stroke="#f8a81c" stroke-width="2.5"/><line x1="5" y1="30" x2="17" y2="30" stroke="#f8a81c" stroke-width="2.5"/></svg>
      <div>
        <div class="speaker-label">SPEAKER</div>
        <div class="speaker-name">TOM VELLING</div>
      </div>
    </div>
  </div>
  <svg class="tri" style="left:317px;top:972px" width="40" height="30" viewBox="0 0 40 30"><polygon points="20,0 40,30 0,30" fill="#f0cf5c"/></svg>

  <div class="block footer-sun"><span class="brand">SD BrightPath</span></div>
  <div class="block footer-sky">
    <div class="register">
      <div class="register-lead">Register now</div>
      <div class="register-url">SdSummitCamp.example</div>
    </div>
  </div>
</div>
</body>
</html>
```